We Need a GREAT Looking Sales Flyer!

Our small, boutique fitness facility needs a new flyer which highlights a new entry level fitness program that we are launching.

The flyer should be visually appealing as we will be handing a full color version to the potential member during our sales process.

I have attached:
- a word document which includes text
-Photos that can be used. Not all need to be used. These are to be used as you feel appropriate
- Our Logo

```html
<!DOCTYPE html>
<html lang="en">
<head>
<meta charset="utf-8">
<title>Corevia – The Ultimate Kickstart Flyer</title>
<link rel="stylesheet" href="https://fonts.googleapis.com/css2?family=Archivo+Black&family=Montserrat:wght@700;800;900&display=swap">
<style>
  :root {
    --backdrop: #202221;
    --ink: #0a0a0a;
    --panel-dark: #1c1c1c;
    --yellow: #f3ee00;
    --white: #ffffff;
    --dot-1: #f5b400;
    --dot-2: #f28a00;
    --dot-3: #f04a00;
    --photo-light: #d9d9d9;
    --photo-mid: #8c8c8c;
    --photo-deep: #3a3a3a;
  }
  * { box-sizing: border-box; margin: 0; padding: 0; }
  html, body { width: 1200px; height: 900px; overflow: hidden; background: var(--backdrop); }
  .canvas { position: relative; width: 1200px; height: 900px; }
  .flyer {
    position: absolute; left: 290px; top: 20px;
    width: 620px; height: 860px; overflow: hidden;
    background: var(--ink);
  }
  .hero-photo {
    position: absolute; left: 0; top: 0; width: 620px; height: 640px;
    background:
      radial-gradient(ellipse 180px 260px at 440px 330px, var(--photo-mid), transparent 70%),
      linear-gradient(135deg, var(--photo-light) 0%, var(--photo-mid) 45%, var(--photo-deep) 100%);
  }
  .shapes { position: absolute; inset: 0; }
  .headline {
    position: absolute; left: 36px; top: 56px;
    font-family: "Archivo Black", sans-serif; font-size: 64px; line-height: .88;
    color: var(--white); text-transform: uppercase; letter-spacing: -1px;
  }
  .program-title {
    position: absolute; left: 32px; top: 262px;
    font-family: "Archivo Black", sans-serif; font-size: 36px; line-height: .92;
    color: var(--yellow); text-transform: uppercase;
  }
  .dots { display: inline-flex; gap: 6px; vertical-align: 6px; margin-left: 8px; }
  .dots span { width: 20px; height: 20px; border-radius: 50%; display: block; }
  .dots span:nth-child(1) { background: var(--dot-1); }
  .dots span:nth-child(2) { background: var(--dot-2); }
  .dots span:nth-child(3) { background: var(--dot-3); }
  .program-claim {
    position: absolute; left: 32px; top: 384px; width: 310px;
    font-family: "Montserrat", sans-serif; font-weight: 800; font-size: 16.5px; line-height: 1.08;
    color: var(--white); text-transform: uppercase;
  }
  .benefits-title {
    position: absolute; left: 32px; top: 478px;
    font-family: "Montserrat", sans-serif; font-weight: 900; font-size: 27px;
    color: var(--yellow); text-transform: uppercase;
  }
  .benefits {
    position: absolute; left: 36px; top: 522px; width: 300px;
    font-family: "Montserrat", sans-serif; font-weight: 700; font-size: 11.5px; line-height: 1.45;
    color: var(--white);
  }
  .benefits p + p { margin-top: 16px; }
  .price {
    position: absolute; left: 32px; top: 742px; width: 320px;
    font-family: "Montserrat", sans-serif; font-weight: 900; font-size: 24px; line-height: 1.05;
    color: var(--yellow); text-transform: uppercase;
  }
  .offer-badge {
    position: absolute; left: 400px; top: 470px; width: 180px;
    font-family: "Montserrat", sans-serif; font-weight: 800; text-transform: uppercase;
  }
  .offer-badge span {
    display: block; width: max-content;
    background: var(--white); color: var(--ink);
    border: 2px solid var(--ink); border-radius: 4px;
    padding: 2px 12px; font-size: 24px; line-height: 1.1;
  }
  .offer-badge span + span { margin: 4px 0 0 10px; }
  .promise {
    position: absolute; left: 372px; top: 612px; width: 240px; text-align: center;
    font-family: "Archivo Black", sans-serif; font-size: 30px; line-height: .95;
    color: var(--yellow); -webkit-text-stroke: 1.5px var(--ink); text-transform: uppercase;
  }
  .brand-name {
    position: absolute; left: 372px; top: 782px; width: 240px; text-align: center;
    font-family: "Montserrat", sans-serif; font-weight: 900; font-size: 38px;
    color: var(--ink);
  }
</style>
</head>
<body>
<main class="canvas">
  <article class="flyer">
    <div class="hero-photo" role="img" aria-label="Black-and-white photo of a woman pressing two dumbbells overhead in a gym"></div>

    <svg class="shapes" width="620" height="860" viewBox="0 0 620 860" aria-hidden="true">
      <rect class="panel-title" x="0" y="248" width="360" height="220" fill="#1c1c1c"/>
      <rect class="panel-benefits" x="0" y="462" width="362" height="398" fill="#0a0a0a"/>
      <polygon class="accent-stripe" points="362,585 620,478 620,500 362,607" fill="#0a0a0a"/>
      <polygon class="offer-panel" points="362,600 620,494 620,860 362,860" fill="#f3ee00"/>
      <line x1="392" y1="596" x2="600" y2="512" stroke="#0a0a0a" stroke-width="2"/>
    </svg>

    <h1 class="headline">Change<br>Begins<br>Now!</h1>

    <h2 class="program-title">The<span class="dots"><span></span><span></span><span></span></span><br>Ultimate<br>Kickstart</h2>

    <p class="program-claim">The fitness program that is responsible for transforming over 924+ lives!</p>

    <h3 class="benefits-title">What you get ?</h3>
    <div class="benefits">
      <p>(1) Unlimited Group Training Designed Specifically to Sculpt &amp; Tone the body. CUSTOM Meal Plan designed specifically for Your and Your Body Type.</p>
      <p>(2) Detailed Body Scans to track results Supplement List to accelerate metabolism 10% off First Supplement Purchase to Kickstart the process Exclusive access to Corevia’s Private Circlehub Page for additional recipes, Support, and Guidance.</p>
    </div>

    <p class="price">Get started for $199 (crossed out) only $99</p>

    <div class="offer-badge"><span>Limited</span><span>Offer</span></div>

    <p class="promise">The life that you envision is possible!</p>

    <p class="brand-name">Corevia</p>
  </article>
</main>
</body>
</html>
```